Building company buisness cards

We are looking for a sharp modern new look for our business cards.
We are a New Zealand based company that specialises in house and land packages.
We have attached a photo of the current logo and would like to see if it can be improved somehow if needed.
We are open to any colours but we have chosen green at this stage.
Feel free to change the font and make the logo smarter looking.
Play with the colours and see what looks best.

We want a card that looks so good know one will want to throw it away!

Target Market(s)

Home buyers

Industry/Entity Type

Building

Contact Information for Business Card

Dorian Keswick
0217392604
dkeswick@tidewellhomecraft.co.nz
tidewellhomecraft.co.nz

Font styles to use
Serif
Sans Serif

Colors

Designer to choose colors to be used in the design.

Requirements
Must have
• Logo and company name on one side, details on the other side
Nice to have
• Color codes for the original green are HEX #4a8028, RGB(74,128,40), CMYK(42,0,69,50)
• Round corners, Raised and/or spot UV

```html
<!DOCTYPE html>
<html lang="en">
<head>
<meta charset="utf-8">
<title>Tidewell Homecraft – Business Card</title>
<link rel="stylesheet" href="https://fonts.googleapis.com/css2?family=Open+Sans:wght@400;700&family=Roboto+Condensed:wght@400&display=swap">
<style>
  :root {
    --brand-green: #4a8028;
    --brand-green-soft: #53893a;
    --muted-green: #a7c79a;
    --paper: #ffffff;
    --backdrop: #ecece8;
  }
  html, body {
    margin: 0;
    padding: 0;
    overflow: hidden;
  }
  .canvas {
    position: relative;
    width: 1200px;
    height: 1200px;
    background: var(--backdrop);
    overflow: hidden;
  }
  .card {
    position: absolute;
    width: 878px;
    height: 515px;
    overflow: hidden;
  }
  .card--front {
    left: 17px;
    top: 58px;
    background: var(--paper);
  }
  .card--back {
    left: 297px;
    top: 641px;
    background: var(--brand-green);
  }
  .front-panel {
    position: absolute;
    left: 0;
    top: 0;
    width: 438px;
    height: 100%;
    background: var(--brand-green);
  }
  .front-panel__art {
    position: absolute;
    left: 20px;
    top: 98px;
    width: 400px;
    height: 320px;
    background: radial-gradient(ellipse at center, var(--brand-green-soft) 0%, var(--brand-green) 72%);
  }
  .holder {
    position: absolute;
    left: 65px;
    top: 210px;
    font-family: "Open Sans", sans-serif;
  }
  .holder__name {
    margin: 0;
    color: var(--paper);
    font-size: 41px;
    font-weight: 400;
    letter-spacing: 3.5px;
    line-height: 1.2;
    white-space: nowrap;
  }
  .holder__role {
    margin: 10px 0 0 2px;
    color: var(--muted-green);
    font-size: 26px;
    letter-spacing: 0.5px;
  }
  .contact-list {
    position: absolute;
    left: 472px;
    top: 155px;
    margin: 0;
    padding: 0;
    list-style: none;
  }
  .contact-item {
    display: flex;
    align-items: center;
    height: 46px;
    margin-bottom: 32px;
    color: var(--brand-green);
  }
  .contact-item__icon {
    width: 46px;
    height: 46px;
    flex: none;
    margin-right: 10px;
  }
  .contact-item__text {
    font-family: "Roboto Condensed", sans-serif;
    font-size: 26px;
    letter-spacing: -0.8px;
    white-space: nowrap;
  }
  .contact-item__text--phone {
    font-family: "Open Sans", sans-serif;
    font-size: 28px;
    letter-spacing: 1.5px;
  }
  .back-pattern {
    position: absolute;
    inset: 0;
    background: linear-gradient(180deg, var(--brand-green-soft) 0%, var(--brand-green) 100%);
  }
  .brand {
    position: absolute;
    left: 0;
    right: 0;
    top: 222px;
    display: flex;
    justify-content: center;
    align-items: center;
    gap: 16px;
    color: var(--paper);
    font-family: "Open Sans", sans-serif;
    font-weight: 700;
    font-size: 44px;
    letter-spacing: -0.5px;
    white-space: nowrap;
  }
  .brand__mark {
    width: 34px;
    height: 34px;
    background: var(--paper);
  }
  .back-url {
    position: absolute;
    left: 0;
    right: 0;
    bottom: 10px;
    margin: 0;
    text-align: center;
    color: var(--paper);
    font-family: "Roboto Condensed", sans-serif;
    font-size: 24px;
    padding-left: 18px;
  }
</style>
</head>
<body>
<div class="canvas">

  <section class="card card--front">
    <div class="front-panel">
      <div class="front-panel__art" role="img" aria-label="Faint decorative house and family illustration"></div>
      <div class="holder">
        <h1 class="holder__name">Dorian Keswick</h1>
        <p class="holder__role">Manager</p>
      </div>
    </div>

    <ul class="contact-list">
      <li class="contact-item">
        <svg class="contact-item__icon" viewBox="0 0 46 46" aria-hidden="true">
          <circle cx="23" cy="23" r="23" fill="#4a8028"/>
          <path d="M11 19 Q23 9 35 19 L32 23 L28 21 L28 18 Q23 16 18 18 L18 21 L14 23 Z" fill="#fff"/>
          <path d="M15 34 L17 24 L29 24 L31 34 Z" fill="#fff"/>
          <circle cx="23" cy="29" r="3" fill="#4a8028"/>
        </svg>
        <span class="contact-item__text contact-item__text--phone">0217392604</span>
      </li>
      <li class="contact-item">
        <svg class="contact-item__icon" viewBox="0 0 46 46" aria-hidden="true">
          <circle cx="23" cy="23" r="23" fill="#4a8028"/>
          <rect x="11" y="14" width="24" height="18" fill="none" stroke="#fff" stroke-width="2.2"/>
          <path d="M11 14 L23 25 L35 14 M11 32 L20 23 M35 32 L26 23" fill="none" stroke="#fff" stroke-width="2"/>
        </svg>
        <span class="contact-item__text">dkeswick@tidewellhomecraft.co.nz</span>
      </li>
      <li class="contact-item">
        <svg class="contact-item__icon" viewBox="0 0 46 46" aria-hidden="true">
          <circle cx="23" cy="23" r="23" fill="#4a8028"/>
          <g fill="none" stroke="#fff" stroke-width="2">
            <circle cx="23" cy="23" r="12"/>
            <ellipse cx="23" cy="23" rx="5.5" ry="12"/>
            <path d="M11 23 H35 M13 17 H33 M13 29 H33"/>
          </g>
        </svg>
        <span class="contact-item__text">www.tidewellhomecraft.co.nz</span>
      </li>
    </ul>
  </section>

  <section class="card card--back">
    <div class="back-pattern" role="img" aria-label="Repeating faint pattern of rooflines and families"></div>
    <div class="brand">
      <span class="brand__mark"></span>
      <span class="brand__name">tidewell homecraft.</span>
    </div>
    <p class="back-url">www.tidewellhomecraft.co.nz</p>
  </section>

</div>
</body>
</html>
```